TALMERA Stationary and Biz Card design
TALMERA Economic Development Company
TALMERA Stationary and Biz Card design - Financial Services
Creative Brief
Professional
Dennis P Wexford
CEO
PO BOX 782 FAIRHOLT, MAINE 04987
dennis@talmeraco.example
talmeraco.example
Looking for designs that encompass the strength and integrity of the logo.

```html
<!DOCTYPE html>
<html lang="en">
<head>
<meta charset="utf-8">
<title>TALMERA Stationery Set</title>
<link rel="stylesheet" href="https://fonts.googleapis.com/css2?family=Cinzel:wght@600&family=Open+Sans:wght@400;600&display=swap">
<style>
  :root {
    --navy: #1f2f5c;
    --paper: #ffffff;
    --backdrop: #e9e6e1;
    --ink: #3a3f4b;
    --rule: #b9bdc6;
    --faint: #e4e6ea;
    --faint-text: #eceef1;
  }
  * { box-sizing: border-box; margin: 0; padding: 0; }
  html, body { width: 1200px; height: 506px; overflow: hidden; }
  body { background: var(--backdrop); font-family: "Open Sans", sans-serif; color: var(--ink); position: relative; }

  .sheet { position: absolute; background: var(--paper); box-shadow: 0 2px 6px rgba(0,0,0,.18); overflow: hidden; }
  .wordmark { font-family: "Cinzel", serif; font-weight: 600; color: var(--navy); letter-spacing: .18em; line-height: 1; }
  .mark-square { display: inline-block; background: var(--navy); vertical-align: middle; }
  .watermark { position: absolute; border-radius: 45% 40% 30% 35%; background: radial-gradient(ellipse at center, #dfe2e8 0%, #eef0f3 60%, rgba(255,255,255,0) 75%); }
  .footer-band { position: absolute; left: 0; right: 0; bottom: 0; background: var(--navy); color: #fff; font-size: 5px; letter-spacing: .08em; display: flex; align-items: center; justify-content: center; }
  .tiny { font-size: 5px; line-height: 1.5; color: var(--ink); }

  /* Envelope back */
  .envelope-back { left: 36px; top: 19px; width: 344px; height: 82px; }
  .envelope-back svg { position: absolute; inset: 0; }
  .envelope-back .wordmark { position: absolute; left: 0; right: 0; top: 20px; text-align: center; color: #fff; font-size: 13px; }

  /* Envelope front small */
  .envelope-front { left: 72px; top: 115px; width: 308px; height: 100px; }
  .envelope-front .wordmark { position: absolute; left: 0; right: 0; top: 20px; text-align: center; font-size: 12px; }

  /* Large envelope */
  .envelope-large { left: 48px; top: 152px; width: 342px; height: 232px; }
  .envelope-large .brand { position: absolute; left: 22px; top: 30px; }
  .envelope-large .wordmark { font-size: 20px; }
  .envelope-large .return { margin-top: 6px; }
  .envelope-large .watermark { right: 18px; top: 96px; width: 150px; height: 110px; }
  .envelope-large .footer-band { height: 16px; }

  /* Letterheads */
  .letterhead { top: 19px; width: 305px; height: 425px; }
  .fax-sheet { left: 494px; }
  .plain-sheet { left: 859px; }
  .letterhead .brand { position: absolute; left: 22px; top: 18px; display: flex; align-items: center; gap: 6px; }
  .letterhead .wordmark { font-size: 12px; }
  .letterhead .contact { position: absolute; right: 22px; top: 18px; text-align: left; }

  .fax-title { position: absolute; left: 22px; top: 70px; font-size: 24px; font-weight: 400; letter-spacing: .02em; color: var(--ink); }
  .fax-fields { position: absolute; left: 22px; top: 110px; width: 262px; display: grid; grid-template-columns: 1fr 1fr; column-gap: 14px; row-gap: 6px; }
  .fax-field { font-size: 6px; border-bottom: .6px solid var(--rule); padding-bottom: 3px; }
  .fax-options { position: absolute; left: 22px; top: 188px; display: flex; gap: 12px; font-size: 5.5px; }
  .fax-options span::before { content: ""; display: inline-block; width: 6px; height: 6px; border: .6px solid var(--ink); margin-right: 3px; vertical-align: -1px; }
  .fax-sheet .watermark { right: 10px; bottom: 22px; width: 150px; height: 110px; }
  .fax-sheet .footer-band { height: 12px; }

  .plain-sheet .watermark { left: 70px; top: 90px; width: 170px; height: 150px; }
  .plain-sheet .ghost-name { position: absolute; left: 0; right: 0; top: 248px; text-align: center; font-family: "Cinzel", serif; font-weight: 600; font-size: 34px; letter-spacing: .2em; color: var(--faint-text); }
  .plain-sheet .base-contact { position: absolute; left: 22px; right: 22px; bottom: 12px; display: flex; justify-content: space-between; }

  .option-label { position: absolute; top: 452px; font-size: 8px; color: #555; }
</style>
</head>
<body>

  <div class="sheet envelope-back">
    <svg width="344" height="82" viewBox="0 0 344 82">
      <polygon points="0,0 344,0 344,14 172,46 0,14" fill="var(--navy)"/>
    </svg>
    <div class="wordmark">TALMERA</div>
  </div>

  <div class="sheet envelope-front">
    <div class="wordmark">TALMERA</div>
  </div>

  <div class="sheet envelope-large">
    <div class="brand">
      <div class="wordmark">TALMERA</div>
      <p class="tiny return">PO BOX 782 FAIRHOLT, MAINE 04987</p>
    </div>
    <div class="watermark" role="img" aria-label="Faint lion emblem decoration"></div>
    <div class="footer-band">www.talmeraco.example</div>
  </div>

  <div class="sheet letterhead fax-sheet">
    <div class="brand"><span class="mark-square" style="width:9px;height:9px"></span><span class="wordmark">TALMERA</span></div>
    <div class="contact tiny">
      <p>T 207 555 0142</p>
      <p>F 207 555 0143</p>
      <p>dennis@talmeraco.example</p>
    </div>
    <h1 class="fax-title">FAX</h1>
    <div class="fax-fields">
      <div class="fax-field">To:</div><div class="fax-field">From:</div>
      <div class="fax-field">Fax:</div><div class="fax-field">Pages:</div>
      <div class="fax-field">Phone:</div><div class="fax-field">Date:</div>
      <div class="fax-field">Re:</div><div class="fax-field">CC:</div>
    </div>
    <div class="fax-options">
      <span>Urgent</span><span>For Review</span><span>Please Comment</span><span>Please Reply</span><span>Please Recycle</span>
    </div>
    <div class="watermark" role="img" aria-label="Faint lion emblem decoration"></div>
    <div class="footer-band">PO BOX 782 FAIRHOLT, MAINE 04987 &nbsp;|&nbsp; talmeraco.example</div>
  </div>
  <p class="option-label" style="left:630px">Option 2</p>

  <div class="sheet letterhead plain-sheet">
    <div class="brand"><span class="mark-square" style="width:9px;height:9px"></span><span class="wordmark">TALMERA</span></div>
    <div class="watermark" role="img" aria-label="Large faint lion emblem decoration"></div>
    <div class="ghost-name">TALMERA</div>
    <div class="base-contact tiny">
      <p>PO BOX 782<br>FAIRHOLT, MAINE 04987</p>
      <p>T 207 555 0142<br>F 207 555 0143</p>
      <p>dennis@talmeraco.example<br>talmeraco.example</p>
    </div>
  </div>
  <p class="option-label" style="left:994px">Option 1</p>

</body>
</html>
```